Business Cards and Stationery for Mobile Ultrasound
Redfern Harbor Mobile Ultrasound
Business Cards and Stationery for Mobile Ultrasound - Medical
Creative Brief
Professional
Marovic Deltrane
P.O Box 827 Quenton CA 95871
mar@rhqx.example
rhqx.example

```html
<!DOCTYPE html>
<html lang="en">
<head>
<meta charset="utf-8">
<title>Redfern Harbor Mobile Ultrasound – Business Card</title>
<link href="https://fonts.googleapis.com/css2?family=Source+Sans+3:wght@400;600;700&display=swap" rel="stylesheet">
<style>
  :root {
    --backdrop: #2f2f30;
    --card-white: #ffffff;
    --brand-purple: #4a2c8f;
    --brand-purple-deep: #3a1f78;
    --brand-green: #2a8a3c;
    --text-light: #ffffff;
  }
  * { margin: 0; padding: 0; box-sizing: border-box; }
  html, body {
    width: 1200px; height: 780px; overflow: hidden;
    background: var(--backdrop);
    font-family: "Source Sans 3", "Myriad Pro", Arial, sans-serif;
  }
  .canvas { position: relative; width: 1200px; height: 780px; }
  .business-card {
    position: absolute; left: 100px; top: 100px;
    width: 1000px; height: 580px;
    background: var(--card-white);
    border-radius: 28px; overflow: hidden;
  }
  .card-sweep { position: absolute; inset: 0; width: 100%; height: 100%; }
  .holder-name {
    position: absolute; left: 56px; top: 118px;
    font-size: 34px; font-weight: 700; color: var(--brand-green);
  }
  .brand-name {
    position: absolute; left: 200px; top: 196px;
    display: flex; align-items: center; gap: 18px;
  }
  .brand-dot {
    width: 40px; height: 40px; border-radius: 50%;
    background: var(--brand-green); flex: none;
  }
  .brand-name span {
    font-size: 40px; font-weight: 600; color: var(--brand-green);
    line-height: 1.05;
  }
  .contact-list {
    position: absolute; right: 44px; top: 312px;
    list-style: none; text-align: right;
    color: var(--text-light); font-size: 21px; font-weight: 400;
  }
  .contact-list li {
    display: flex; justify-content: flex-end; align-items: center;
    gap: 14px; height: 34px;
  }
  .contact-list svg { width: 22px; height: 22px; }
  .postal-address {
    position: absolute; right: 44px; top: 432px;
    color: var(--text-light); font-size: 21px;
  }
</style>
</head>
<body>
<div class="canvas">
  <div class="business-card">
    <svg class="card-sweep" viewBox="0 0 1000 580" preserveAspectRatio="none" aria-hidden="true">
      <defs>
        <linearGradient id="purpleBand" x1="0" y1="1" x2="1" y2="0">
          <stop offset="0" stop-color="#3a1f78"/>
          <stop offset="1" stop-color="#4a2c8f"/>
        </linearGradient>
      </defs>
      <path d="M0,548 C420,530 720,360 800,0 L1000,0 L1000,580 L0,580 Z" fill="url(#purpleBand)"/>
      <path d="M0,528 C405,510 700,345 775,0" fill="none" stroke="#2a8a3c" stroke-width="7"/>
    </svg>

    <p class="holder-name">Marovic Deltrane</p>

    <div class="brand-name">
      <div class="brand-dot"></div>
      <span>Redfern Harbor<br>Mobile Ultrasound</span>
    </div>

    <ul class="contact-list">
      <li>5550127846
        <svg viewBox="0 0 24 24" fill="#fff"><path d="M6.6 10.8a15 15 0 0 0 6.6 6.6l2.2-2.2c.3-.3.7-.4 1-.2 1.1.4 2.3.6 3.6.6.6 0 1 .4 1 1V20c0 .6-.4 1-1 1A17 17 0 0 1 3 4c0-.6.4-1 1-1h3.5c.6 0 1 .4 1 1 0 1.3.2 2.5.6 3.6.1.3 0 .7-.2 1z"/></svg>
      </li>
      <li>mar@rhqx.example
        <svg viewBox="0 0 24 24" fill="none" stroke="#fff" stroke-width="2"><rect x="3" y="5" width="18" height="14" rx="2"/><path d="M3 7l9 6 9-6"/></svg>
      </li>
      <li>www.rhqx.example
        <svg viewBox="0 0 24 24" fill="none" stroke="#fff" stroke-width="1.8"><circle cx="12" cy="12" r="9"/><ellipse cx="12" cy="12" rx="4" ry="9"/><path d="M3 12h18M5 7h14M5 17h14"/></svg>
      </li>
    </ul>

    <p class="postal-address">P.O Box 827, Quenton CA 95871</p>
  </div>
</div>
</body>
</html>
```